Business Card Design Project

Hello,

We need a business card, which will be presented the our company Studio Lopatka and its brand Framehaul.
Studio Lopatka is a video production company.
Stock video footage Framehaul is a trademark of Studio Lopatka.
We need a designer that will set both the logo and contacts on the card. Print will be executed on a single page, it will use a translucent paper.

Contacts:

Tadej Bremec
Founder and CEO

Studio Lopatka d.o.o., Pot na Slivnik 14, 8000 Novo mesto, Slovenia
T: +386 599 81 316, M: +386 41 203 659
tadej@lopatka-example.si, www.lopatka-example.si
info@framehaul-example.com, www.framehaul-example.com

In the attachment are located both logo!

Thanks in advance,

Tadej

```html
<!DOCTYPE html>
<html lang="en">
<head>
<meta charset="utf-8">
<title>Studio Lopatka – Business Card</title>
<link rel="stylesheet" href="https://fonts.googleapis.com/css2?family=Arimo:wght@300;400;700&display=swap">
<style>
  :root {
    --page: #ffffff;
    --card: #ffffff;
    --card-edge: #2b2b2b;
    --studio-grey: #7a7a7a;
    --mark-dark: #333333;
    --accent-orange: #e8762d;
    --brand-blue: #1e88d0;
    --name-blue: #3a6fb5;
    --brand-square: #e03a4e;
    --footer-grey: #cbcbcd;
    --ink: #111111;
  }
  html, body {
    margin: 0;
    width: 1200px;
    height: 1000px;
    overflow: hidden;
    background: var(--page);
    font-family: "Arimo", Arial, sans-serif;
  }
  .stage {
    position: relative;
    width: 1200px;
    height: 1000px;
  }
  .business-card {
    position: absolute;
    left: 406px;
    top: 161px;
    width: 388px;
    height: 678px;
    background: var(--card);
    outline: 1px solid var(--card-edge);
    box-shadow: 0 6px 14px rgba(0,0,0,0.18);
  }
  .business-card svg { display: block; }
  .studio-name { font-weight: 300; fill: var(--studio-grey); letter-spacing: 1px; }
  .web-link { fill: var(--accent-orange); }
  .brand-name { font-weight: 700; fill: var(--brand-blue); }
  .person-name { fill: var(--name-blue); }
  .person-role, .contact-line { fill: var(--ink); }
</style>
</head>
<body>
<main class="stage">
  <article class="business-card">
    <svg width="388" height="678" viewBox="0 0 388 678" font-family="Arimo, Arial, sans-serif">
      <defs>
        <linearGradient id="pastel-field" x1="0" y1="0" x2="1" y2="1">
          <stop offset="0" stop-color="#e6f2e0"/>
          <stop offset="0.4" stop-color="#e3eff8"/>
          <stop offset="0.7" stop-color="#fbf6dc"/>
          <stop offset="1" stop-color="#fbe7ea"/>
        </linearGradient>
      </defs>

      <!-- Studio header -->
      <circle cx="194" cy="52" r="22" fill="var(--mark-dark)"/>
      <text class="studio-name" x="194" y="104" text-anchor="middle" font-size="34">Studio Lopatka</text>
      <text class="web-link" x="194" y="130" text-anchor="middle" font-size="16">www.lopatka-example.si</text>

      <!-- Brand area -->
      <rect x="0" y="185" width="280" height="210" fill="url(#pastel-field)" opacity="0.7"
            role="img" aria-label="Soft pastel squares in green, blue, yellow and pink"/>
      <rect x="30" y="228" width="34" height="34" fill="var(--brand-square)"/>
      <text class="brand-name" x="80" y="258" font-size="32">Framehaul</text>
      <text class="web-link" x="194" y="295" text-anchor="middle" font-size="16">www.framehaul-example.com</text>

      <!-- Contact footer -->
      <polygon points="0,512 388,415 388,678 0,678" fill="var(--footer-grey)"/>
      <polygon points="0,442 232,384 245,447 0,510" fill="var(--accent-orange)"/>

      <g transform="translate(24,468) rotate(-14)">
        <text class="person-name" x="0" y="0" font-size="22">Tadej Bremec</text>
        <text class="person-role" x="22" y="20" font-size="16">Founder and CEO</text>
      </g>

      <g transform="translate(191,503) rotate(-14)" font-size="17" text-anchor="middle">
        <text class="contact-line" x="0" y="0">Pot na Slivnik 14</text>
        <text class="contact-line" x="0" y="21">8000 Novo mesto, Slovenia</text>
        <text class="contact-line" x="0" y="58">T: +386 599 81 316</text>
        <text class="contact-line" x="0" y="79">M: +386 41 203 659</text>
        <text class="contact-line" x="0" y="116">tadej@lopatka-example.si</text>
        <text class="contact-line" x="0" y="137">info@framehaul-example.com</text>
      </g>
    </svg>
  </article>
</main>
</body>
</html>
```